Steel Company / Iron Railing Business Card Template

We are a custom steel fabrication company located in Halden, PA. In business since 1979, we recently developed a new logo, and we're looking for a business card design to help display the new logo and our business. The name of the company is Kelbrook Forge Co.. The Office Phone number is (610) 555-0143. We fabricate and install custom "wrought iron" railings on our residential side, we also fabricate and erect structural steel (think cranes and steel beams in buildings) on our commercial side. Looking to get a business card template designed. Something modern, but professional. Clear and easy to read. Front should have all business and employee information including phone number(s), email address, business information, etc. back should spotlight logo.

Industry/Entity Type

Construction / Home Improvement

Contact Information for Business Card

Business information is Kelbrook Forge Co., 48 Dunmore Ave Suite 3305, Halden, PA 19074. Phone number is (610) 555-0143. Website is www.kelbrookforge.example Business card should be for "Tom Pelling" with the job title "Sales & Estimating" but be editable for other employees. Tom's phone number is (610) 555-0178

Colors

Designer to choose colors to be used in the design.

Requirements
Must have
• Modern Feel, Design should be sized for standard business card sizing 3.5" x 2" (88.9mm x 50.8mm)

```html
<!DOCTYPE html>
<html lang="en">
<head>
<meta charset="utf-8">
<title>Kelbrook Forge Co. — Business Card</title>
<link rel="stylesheet" href="https://fonts.googleapis.com/css2?family=Anton&family=Poppins:wght@400;500;600&display=swap">
<style>
  :root {
    --backdrop: #1c1c1e;
    --card: #141415;
    --ink-white: #f2f2f2;
    --brand-blue: #2a47a8;
    --brand-red: #d8202a;
    --emboss: #3d3d40;
  }
  * { box-sizing: border-box; margin: 0; padding: 0; }
  html, body {
    width: 1200px; height: 820px; overflow: hidden;
    background: radial-gradient(ellipse at 50% 40%, #2a2a2c 0%, var(--backdrop) 70%);
    font-family: "Poppins", sans-serif;
  }
  .canvas {
    width: 1200px; height: 820px;
    display: flex; align-items: center; justify-content: center; gap: 40px;
  }
  .card {
    position: relative;
    width: 540px; height: 309px;
    background: var(--card);
    border-left: 3px solid var(--brand-red);
    border-bottom: 3px solid var(--brand-red);
    box-shadow: 0 18px 40px rgba(0,0,0,.55);
  }
  .card--back { border: 3px solid var(--brand-red); }

  /* front */
  .accent-bar {
    position: absolute; left: 0; top: 44px;
    width: 12px; height: 46px; background: var(--brand-red);
  }
  .employee { position: absolute; left: 34px; top: 34px; }
  .employee__name {
    font-family: "Anton", sans-serif; font-size: 24px; letter-spacing: .5px;
    color: var(--brand-blue); text-transform: uppercase; line-height: 1.05;
  }
  .employee__title { font-size: 14px; color: var(--brand-red); line-height: 1.3; }
  .contact-line {
    display: flex; align-items: center; gap: 7px;
    font-size: 14px; color: var(--ink-white); line-height: 1.45;
  }
  .contact-line svg { width: 13px; height: 13px; flex: none; }

  .brand-mark {
    position: absolute; right: 30px; top: 50px;
    display: flex; align-items: center; gap: 9px;
  }
  .brand-mark__dot { width: 14px; height: 14px; border-radius: 50%; background: var(--brand-red); }
  .brand-mark__name {
    font-family: "Poppins", sans-serif; font-weight: 600; font-size: 24px;
    color: var(--brand-blue); line-height: 1;
  }

  .office-address {
    position: absolute; right: 24px; top: 168px; text-align: right;
    font-size: 13px; color: var(--ink-white); line-height: 1.4; font-style: normal;
  }
  .office-address__company { color: var(--brand-blue); font-weight: 500; }

  .office-contact { position: absolute; left: 56px; bottom: 22px; }

  /* back */
  .back-mark {
    position: absolute; inset: 0;
    display: flex; align-items: center; justify-content: center; gap: 14px;
  }
  .back-mark__dot { width: 22px; height: 22px; border-radius: 50%; background: var(--emboss); }
  .back-mark__name {
    font-family: "Poppins", sans-serif; font-weight: 600; font-size: 38px;
    color: var(--emboss);
  }
</style>
</head>
<body>
<main class="canvas">

  <section class="card card--front" aria-label="Business card front">
    <div class="accent-bar"></div>
    <div class="employee">
      <p class="employee__name">Tom Pelling</p>
      <p class="employee__title">Sales &amp; Estimating</p>
      <p class="contact-line">
        <svg viewBox="0 0 24 24" fill="var(--brand-blue)"><path d="M6.6 10.8a15.1 15.1 0 0 0 6.6 6.6l2.2-2.2a1 1 0 0 1 1-.25 11.4 11.4 0 0 0 3.6.57 1 1 0 0 1 1 1V20a1 1 0 0 1-1 1A17 17 0 0 1 3 4a1 1 0 0 1 1-1h3.5a1 1 0 0 1 1 1c0 1.25.2 2.45.57 3.57a1 1 0 0 1-.25 1z"/></svg>
        (610) 555-0178
      </p>
    </div>

    <div class="brand-mark">
      <span class="brand-mark__dot"></span>
      <span class="brand-mark__name">Kelbrook Forge Co.</span>
    </div>

    <address class="office-address">
      <p class="office-address__company">Kelbrook Forge Co.</p>
      <p>48 Dunmore Ave Suite 3305</p>
      <p>Halden, PA 19074</p>
    </address>

    <div class="office-contact">
      <p class="contact-line">
        <svg viewBox="0 0 24 24" fill="var(--brand-blue)"><path d="M6.6 10.8a15.1 15.1 0 0 0 6.6 6.6l2.2-2.2a1 1 0 0 1 1-.25 11.4 11.4 0 0 0 3.6.57 1 1 0 0 1 1 1V20a1 1 0 0 1-1 1A17 17 0 0 1 3 4a1 1 0 0 1 1-1h3.5a1 1 0 0 1 1 1c0 1.25.2 2.45.57 3.57a1 1 0 0 1-.25 1z"/></svg>
        (610) 555-0143
      </p>
      <p class="contact-line">
        <svg viewBox="0 0 24 24" fill="var(--brand-blue)"><path d="M2 5h20v14H2z M2 5l10 8 10-8" stroke="var(--card)" stroke-width="1.5"/></svg>
        info@kelbrookforge.example
      </p>
      <p class="contact-line">
        <svg viewBox="0 0 24 24" fill="none" stroke="var(--brand-blue)" stroke-width="2"><circle cx="12" cy="12" r="10"/><path d="M2 12h20M12 2c3 3 3 17 0 20M12 2c-3 3-3 17 0 20"/></svg>
        www.kelbrookforge.example
      </p>
    </div>
  </section>

  <section class="card card--back" aria-label="Business card back">
    <div class="back-mark">
      <span class="back-mark__dot"></span>
      <span class="back-mark__name">Kelbrook Forge Co.</span>
    </div>
  </section>

</main>
</body>
</html>
```